"End of year wishes" - Electronic card

Velmora is a regulatory consulting company in the cosmetic sector. We provide premium services and have 12 years of experience.
Please visit our website for more information: https://velmora-example.com
Like every year, we would like to send an electronic design to our clients and partners to wish them happy holidays. This year, we would like to share two good news with them: offer them a surprise (to be revealed later on) and invite them to visit our new brand new website. We relay on your talent and imagination for the design! We need something very professional, serious, beautiful and in line with our graphic layout (see our company website)

Target Market(s)

cosmetic brands

Industry/Entity Type

Cosmetics

Requirements
Must have
• The following statement should be included to the design:

We wish you a Happy Holiday and a Marvelous New Year 2021!
As December is the month of giving, we have a surprise for you. Please contact your dedicated Account Manager to find out more!

Good news never comes alone, we've also updated our website in order to serve you better. We hope you like it as much as we do.
Please enjoy the experience: www.velmora-example.com

```html
<!DOCTYPE html>
<html lang="en">
<head>
<meta charset="utf-8">
<title>Velmora – Season's Greetings 2021</title>
<link rel="stylesheet" href="https://fonts.googleapis.com/css2?family=Pinyon+Script&family=Raleway:wght@300;600&display=swap">
<style>
  :root {
    --green-center: #46a352;
    --green-mid: #2f7a37;
    --green-edge: #1f5826;
    --text-light: #ffffff;
    --snow: #f1f4f2;
    --snow-shade: #dfe5e1;
    --footer-text: #3c3f3d;
  }
  * { margin: 0; padding: 0; box-sizing: border-box; }
  html, body {
    width: 848px;
    height: 1200px;
    overflow: hidden;
  }
  body {
    background: var(--green-edge);
    font-family: "Raleway", sans-serif;
  }
  .card {
    position: relative;
    width: 848px;
    height: 1200px;
    overflow: hidden;
    background: radial-gradient(ellipse 75% 60% at 50% 52%, var(--green-center) 0%, var(--green-mid) 55%, var(--green-edge) 100%);
    color: var(--text-light);
    text-align: center;
  }
  .brand {
    position: absolute;
    top: 52px;
    left: 0;
    width: 100%;
    font-weight: 600;
    font-size: 40px;
    letter-spacing: 0.01em;
    line-height: 44px;
  }
  .greeting {
    position: absolute;
    top: 150px;
    left: 0;
    width: 100%;
    font-weight: 300;
  }
  .greeting .script {
    display: block;
    font-family: "Pinyon Script", cursive;
    font-weight: 400;
    font-size: 44px;
    line-height: 60px;
    letter-spacing: 0.04em;
  }
  .greeting .plain {
    display: block;
    font-size: 31px;
    line-height: 59px;
    letter-spacing: 0.09em;
  }
  .message {
    position: absolute;
    left: 0;
    width: 100%;
    font-weight: 300;
    font-size: 27px;
    line-height: 50px;
    letter-spacing: 0.07em;
  }
  .message--surprise { top: 440px; }
  .message--website { top: 720px; }
  .winter-scene {
    position: absolute;
    left: 0;
    bottom: 0;
    width: 100%;
    height: 190px;
    background: linear-gradient(to bottom, rgba(241,244,242,0) 0%, rgba(241,244,242,0.55) 30%, var(--snow-shade) 55%, var(--snow) 100%);
  }
  .site-link {
    position: absolute;
    left: 0;
    bottom: 22px;
    width: 100%;
    font-weight: 300;
    font-size: 19px;
    letter-spacing: 0.14em;
    color: var(--footer-text);
    text-decoration: none;
  }
</style>
</head>
<body>
  <main class="card">
    <div class="brand">velmora</div>

    <h1 class="greeting">
      <span class="script">We wish</span>
      <span class="plain">you a Happy Holiday</span>
      <span class="plain">and a Marvelous</span>
      <span class="script">New Year 2021!</span>
    </h1>

    <p class="message message--surprise">
      As December is the month of<br>
      giving, we have a<br>
      surprise for you. Please contact<br>
      your dedicated Account Manager<br>
      to find out more!
    </p>

    <p class="message message--website">
      Good news never comes alone,<br>
      we've also updated our website<br>
      in order to serve you better.<br>
      We hope you like it as much as we do.<br>
      Please enjoy the experience:
    </p>

    <div class="winter-scene" role="img" aria-label="Snowy landscape with white pine trees and a small house"></div>

    <a class="site-link" href="https://velmora-example.com">www.velmora-example.com</a>
  </main>
</body>
</html>
```